Bright Builders WA Ball Poster

To Create a Poster for the Bright Builders WA Ball 2013

Target Market(s)

Young Professional Engineers aged 18-35. Male and Female

Requirements
Must have
• All Details required for the ball. Black and white/silver theme. Some kind of engineering theme. Must have the following text:

Join us in celebrating the Annual Bright Builders of Western Australia Ball with a night of dinner and entertainment.
Saturday July 13th, 2013
Time: 7pm Arrival
Venue: Corvane Ashby Hotel, Perth
Dress: Formal
The evening will include drinks, a three-course dinner, music and dancing.
Ticket price $139, on sale now! To purchase tickets go to:
(website to be announced)
Proceeds go to Makers Across Frontiers
is is an 18+ event. Open to general public.
Nice to have
• Modern, Classy, Similar to previous years designs. Possibly Masquerade themed.
Should not have
• Fish, environmental theme, rural Australia theme (these have been done)

```html
<!DOCTYPE html>
<html lang="en">
<head>
<meta charset="utf-8">
<title>Bright Builders WA Ball 2013</title>
<link rel="stylesheet" href="https://fonts.googleapis.com/css2?family=Fira+Sans:wght@400;500;600;700&family=Libre+Baskerville:ital,wght@1,400;1,700&display=swap">
<style>
  :root {
    --backdrop: #ececec;
    --poster: #000000;
    --ink: #ffffff;
    --ink-soft: #e6e6e6;
    --rule: #8a8a8a;
    --mask-light: #e4e4e4;
    --mask-mid: #9a9a9a;
    --mask-dark: #000000;
    --partner-slot: #5b5b5d;
    --partner-bg: #ffffff;
    --partner-ink: #222222;
    --accent: #e0262b;
  }
  * { margin: 0; padding: 0; box-sizing: border-box; }
  html, body { width: 1200px; height: 900px; overflow: hidden; background: var(--backdrop); }
  .canvas { position: relative; width: 1200px; height: 900px; }
  .poster {
    position: absolute; left: 297px; top: 22px; width: 607px; height: 858px;
    background: var(--poster); color: var(--ink); text-align: center;
    font-family: "Fira Sans", sans-serif;
  }
  .abs { position: absolute; left: 0; width: 100%; white-space: nowrap; }
  .serif-italic { font-family: "Libre Baskerville", serif; font-style: italic; }
  .invite { top: 37px; font-size: 21px; line-height: 28px; }
  .title { top: 67px; font-size: 40px; font-weight: 600; line-height: 46px; letter-spacing: -0.2px; }
  .subtitle { top: 161px; font-size: 21px; line-height: 28px; }
  .mask-art {
    position: absolute; left: 83px; top: 208px; width: 436px; height: 270px;
  }
  .highlights { top: 478px; font-size: 19px; font-weight: 500; line-height: 27px; }
  .rule { position: absolute; left: 161px; width: 277px; height: 1px; background: var(--rule); }
  .rule.top { top: 541px; }
  .rule.bottom { top: 600px; }
  .tickets { top: 548px; font-size: 14.5px; line-height: 20px; color: var(--ink-soft); }
  .site { top: 568px; font-size: 19px; font-weight: 700; line-height: 24px; }
  .proceeds { top: 607px; font-size: 15px; line-height: 21px; color: var(--ink-soft); }
  .proceeds b { font-family: "Fira Sans", sans-serif; font-style: normal; font-weight: 700; }
  .date {
    position: absolute; left: 70px; top: 668px; width: 76px;
    font-size: 15.5px; font-weight: 600; line-height: 20px;
  }
  .date sup { font-size: 9px; }
  .details {
    position: absolute; left: 152px; top: 668px; text-align: left;
    font-size: 14.5px; font-weight: 500; line-height: 20px;
  }
  .details .label { font-family: "Libre Baskerville", serif; font-style: italic; font-weight: 400; font-size: 13px; }
  .org {
    position: absolute; left: 424px; top: 678px; display: flex; align-items: center; gap: 8px;
    font-size: 13px; font-weight: 500; color: var(--ink); text-align: left;
  }
  .org .mark { width: 22px; height: 22px; background: var(--accent); }
  .partners {
    position: absolute; left: 74px; top: 741px; width: 457px; height: 76px;
    background: var(--partner-bg); color: var(--partner-ink); text-align: left;
  }
  .partners h2 { position: absolute; left: 10px; top: 6px; font-size: 10px; font-weight: 600; }
  .partner-slot { position: absolute; top: 27px; width: 115px; height: 43px; background: var(--partner-slot); }
  .partner-slot:nth-of-type(1) { left: 10px; }
  .partner-slot:nth-of-type(2) { left: 171px; }
  .partner-slot:nth-of-type(3) { left: 332px; }
</style>
</head>
<body>
<div class="canvas">
  <article class="poster">
    <p class="abs invite serif-italic">Join us in celebrating the</p>
    <h1 class="abs title">Annual Bright Builders<br>of Western Australia Ball</h1>
    <p class="abs subtitle serif-italic">with a night of dinner and entertainment.</p>

    <svg class="mask-art" viewBox="0 0 436 270" role="img" aria-label="Masquerade mask made of interlocking silver engineering gears, with a faint reflection below">
      <defs>
        <radialGradient id="maskTone" cx="50%" cy="40%" r="55%">
          <stop offset="0%" stop-color="var(--mask-light)"/>
          <stop offset="55%" stop-color="var(--mask-mid)"/>
          <stop offset="100%" stop-color="var(--mask-dark)"/>
        </radialGradient>
      </defs>
      <rect x="0" y="0" width="436" height="270" fill="url(#maskTone)"/>
    </svg>

    <p class="abs highlights">The evening will include drinks,<br>a three-course dinner, music and dancing.</p>
    <div class="rule top"></div>
    <p class="abs tickets serif-italic">Ticket price $139, on sale now! To purchase tickets go to:</p>
    <p class="abs site">www.buildersball.org.au</p>
    <div class="rule bottom"></div>
    <p class="abs proceeds serif-italic">Proceeds go to Makers Across Frontiersis an <b>18+</b> event.<br>Open to general public.</p>

    <p class="date">Saturday<br>July 13<sup>th</sup><br>2013</p>
    <p class="details">
      <span class="label">Time:</span> 7pm Arrival<br>
      <span class="label">Venue:</span> Corvane Ashby Hotel, Perth<br>
      <span class="label">Dress:</span> Formal
    </p>
    <div class="org"><span class="mark"></span><span>Structa Guild</span></div>

    <section class="partners">
      <h2>Partners</h2>
      <div class="partner-slot"></div>
      <div class="partner-slot"></div>
      <div class="partner-slot"></div>
    </section>
  </article>
</div>
</body>
</html>
```